KTR Engineering Pty Ltd

I have already had Corvale welding and fabrication cards made , my business has changed too KTR engineering Pty Ltd so I need my logo changed on the cards
one side have my logo then the other side have what we do.
front side logo and details
owner /operator : Lachlan Meravic
email: ktr.works@ironvalemail.com
number: 0491537204
ABN: 47 261 538 902
ACN: 718 352 946
on back have in dot points what we do:
* structural steel erection
* precast panels
* site welding
*steel alteration & repair
* rigging & dogging
*labour hire
all details in breif

```html
<!DOCTYPE html>
<html lang="en">
<head>
<meta charset="utf-8">
<title>KTR Engineering Pty Ltd — Business Cards</title>
<link rel="stylesheet" href="https://fonts.googleapis.com/css2?family=Arimo:wght@400;700&display=swap">
<style>
  :root {
    --navy: #13223a;
    --navy-deep: #0f2035;
    --rust: #9a433d;
    --white: #ffffff;
    --grey: #6b6f76;
    --stage: #e9eaec;
  }
  * { box-sizing: border-box; margin: 0; padding: 0; }
  html, body { width: 1200px; height: 959px; overflow: hidden; }
  body {
    background: var(--stage);
    font-family: "Arimo", Arial, sans-serif;
    display: flex;
    flex-direction: column;
    align-items: center;
    justify-content: center;
    gap: 70px;
  }
  .card {
    position: relative;
    width: 620px;
    height: 354px;
    overflow: hidden;
    box-shadow: 0 10px 30px rgba(0,0,0,0.18);
  }

  /* Back: services */
  .card--back { background: var(--navy); color: var(--white); }
  .brand-name {
    font-weight: 700;
    text-transform: uppercase;
    letter-spacing: 0.5px;
    line-height: 1.05;
  }
  .card--back .brand-name {
    position: absolute;
    left: 48px;
    top: 138px;
    width: 230px;
    font-size: 30px;
    color: var(--white);
  }
  .card--back .divider {
    position: absolute;
    left: 300px;
    top: 110px;
    width: 1px;
    height: 150px;
    background: var(--rust);
  }
  .services-title {
    position: absolute;
    left: 300px;
    top: 62px;
    width: 210px;
    text-align: center;
    font-weight: 700;
    font-size: 17px;
    letter-spacing: 0.5px;
  }
  .services {
    position: absolute;
    left: 324px;
    top: 112px;
    list-style: none;
    font-size: 15px;
    line-height: 24.5px;
  }
  .services li::before {
    content: "";
    display: inline-block;
    width: 4px;
    height: 4px;
    border-radius: 50%;
    background: var(--rust);
    margin-right: 7px;
    vertical-align: middle;
  }

  /* Front: contact */
  .card--front { background: var(--navy-deep); }
  .card--front .sweep { position: absolute; inset: 0; }
  .card--front .brand {
    position: absolute;
    right: 40px;
    top: 62px;
    display: flex;
    align-items: center;
    gap: 10px;
  }
  .card--front .brand-mark {
    width: 14px;
    height: 14px;
    border-radius: 50%;
    background: var(--rust);
  }
  .card--front .brand-name {
    font-size: 28px;
    color: var(--navy);
    width: 250px;
  }
  .registry {
    position: absolute;
    right: 44px;
    top: 196px;
    font-size: 14px;
    line-height: 20px;
    color: var(--grey);
  }
  .registry b { color: var(--navy); }
  .contact {
    position: absolute;
    left: 40px;
    bottom: 34px;
    color: var(--white);
  }
  .contact .person {
    font-size: 22px;
    font-weight: 700;
    text-transform: uppercase;
    letter-spacing: 0.5px;
    color: var(--rust);
  }
  .contact .role { font-size: 15px; margin: 4px 0 12px; }
  .contact .line {
    display: flex;
    align-items: center;
    gap: 9px;
    font-size: 15px;
    line-height: 22px;
  }
  .contact .line svg { width: 13px; height: 13px; fill: var(--rust); }
</style>
</head>
<body>

  <section class="card card--back" aria-label="Card back: services">
    <p class="brand-name">KTR Engineering Pty Ltd</p>
    <span class="divider"></span>
    <h2 class="services-title">WHAT WE DO</h2>
    <ul class="services">
      <li>Structural steel erection</li>
      <li>Precast panels</li>
      <li>Site welding</li>
      <li>Steel alteration &amp; repair</li>
      <li>Rigging &amp; dogging</li>
      <li>Labour hire</li>
    </ul>
  </section>

  <section class="card card--front" aria-label="Card front: contact details">
    <svg class="sweep" viewBox="0 0 620 354" preserveAspectRatio="none" aria-hidden="true">
      <path d="M205 0 Q280 318 620 320 L620 0 Z" fill="#9a433d"/>
      <path d="M213 0 Q290 308 620 310 L620 0 Z" fill="#ffffff"/>
    </svg>

    <div class="brand">
      <span class="brand-mark"></span>
      <p class="brand-name">KTR Engineering Pty Ltd</p>
    </div>

    <p class="registry"><b>ABN:</b> 47 261 538 902<br><b>ACN:</b> 718 352 946</p>

    <div class="contact">
      <p class="person">Lachlan Meravic</p>
      <p class="role">Owner / Operator</p>
      <p class="line">
        <svg viewBox="0 0 24 24" aria-hidden="true"><path d="M6.6 10.8a15.1 15.1 0 0 0 6.6 6.6l2.2-2.2a1 1 0 0 1 1-.25 11.4 11.4 0 0 0 3.6.57 1 1 0 0 1 1 1V20a1 1 0 0 1-1 1A17 17 0 0 1 3 4a1 1 0 0 1 1-1h3.5a1 1 0 0 1 1 1c0 1.25.2 2.45.57 3.57a1 1 0 0 1-.25 1z"/></svg>
        0491537204
      </p>
      <p class="line">
        <svg viewBox="0 0 24 24" aria-hidden="true"><path d="M2 5h20v14H2z M4 7v.5l8 5 8-5V7l-8 5z"/></svg>
        ktr.works@ironvalemail.com
      </p>
    </div>
  </section>

</body>
</html>
```